Tunnel

a graphic meme to be sent to my clients, consisting of a long angular dark tunnel with a bright light at one end; located within the bright light at the end of the tunnel is the number 2021
the illuminated (shiny silver?) 3 dimensional font message running along the left wall of the tunnel is: BE SAFE.!
the smaller font message underneath the graphic is: Best Wishes For a Healthy New Year
Dan Marlowe Mediator (also to be included nearby is a small semi-circle logo of my corporate logo).

Font styles to use
Sans Serif
Other font styles liked:
• 3 dimensional bold lettering for BE SAFE

```html
<!DOCTYPE html>
<html lang="en">
<head>
<meta charset="utf-8">
<title>Be Safe – New Year Greeting</title>
<link rel="stylesheet" href="https://fonts.googleapis.com/css2?family=Anton&family=Cinzel+Decorative:wght@400;700&family=Libre+Baskerville:wght@400&display=swap">
<style>
  :root {
    --tunnel-dark: #060606;
    --tunnel-mid: #2a2a2a;
    --tunnel-light: #f4f4ef;
    --gold: #d6a11c;
    --gold-deep: #7c5a0c;
    --gold-band: #f2b31a;
    --navy: #13085a;
    --white: #ffffff;
    --rule: #9c9c9c;
    --photo-grey: #8e939a;
  }
  * { margin: 0; padding: 0; box-sizing: border-box; }
  html, body {
    width: 892px; height: 1200px; overflow: hidden; background: var(--white);
  }
  .card {
    position: relative; width: 892px; height: 1200px; overflow: hidden;
    background: var(--navy);
  }
  .tunnel-photo {
    position: absolute; left: 0; top: 0; width: 892px; height: 980px;
    background:
      radial-gradient(ellipse 170px 260px at 705px 560px, var(--tunnel-light) 0%, #cfcfc8 25%, #6a6a66 55%, rgba(20,20,20,0) 100%),
      radial-gradient(ellipse 520px 420px at 560px 540px, #3a3a38 0%, #1a1a1a 55%, var(--tunnel-dark) 100%),
      var(--tunnel-dark);
  }
  .headline {
    position: absolute; left: 82px; top: 430px;
    font-family: "Anton", "Impact", sans-serif;
    font-size: 215px; line-height: 1; letter-spacing: 2px;
    color: var(--gold);
    transform-origin: left center;
    transform: perspective(900px) rotateY(38deg);
    text-shadow:
      2px 2px 0 var(--gold-deep), 4px 4px 0 var(--gold-deep),
      6px 6px 0 var(--gold-deep), 8px 8px 0 var(--gold-deep),
      10px 10px 14px rgba(0,0,0,.6);
    white-space: nowrap;
  }
  .greeting {
    position: absolute; left: 0; width: 924px; top: 736px;
    text-align: center;
    font-family: "Cinzel Decorative", serif;
    font-size: 45px; line-height: 60px; letter-spacing: 1px;
    color: var(--gold);
  }
  .greeting-rule {
    position: absolute; left: 293px; top: 879px; width: 262px; height: 2px;
    background: var(--rule);
  }
  .band { position: absolute; left: 0; top: 900px; width: 892px; height: 300px; }
  .portrait {
    position: absolute; left: 78px; top: 1001px; width: 131px; height: 150px;
    border: 4px solid var(--white);
    background: linear-gradient(180deg, #b7bcc2 0%, var(--photo-grey) 60%, #3b3f48 100%);
  }
  .contact {
    position: absolute; left: 231px; top: 1034px;
    font-family: "Libre Baskerville", serif; color: var(--white);
  }
  .contact-name { font-size: 29px; letter-spacing: 3px; line-height: 34px; }
  .contact-role { font-size: 15px; letter-spacing: 1.5px; color: var(--gold); margin-top: 2px; }
  .contact-detail { font-size: 15px; letter-spacing: 1.5px; line-height: 26px; }
  .contact-email { margin-top: 16px; }
  .firm {
    position: absolute; left: 628px; top: 1040px; width: 200px;
    display: flex; align-items: center; gap: 12px;
    font-family: "Libre Baskerville", serif; font-size: 20px; line-height: 28px;
    color: var(--gold);
  }
  .firm-mark {
    flex: none; width: 34px; height: 34px; border-radius: 50%;
    border: 3px solid var(--gold);
  }
</style>
</head>
<body>
  <main class="card">
    <div class="tunnel-photo" role="img" aria-label="Long dark rocky tunnel with bright light at its far end"></div>

    <h1 class="headline">BE SAFE</h1>

    <p class="greeting">Best Wishes for a<br>Healthy New Year!</p>
    <div class="greeting-rule"></div>

    <svg class="band" viewBox="0 0 892 300" width="892" height="300" aria-hidden="true">
      <polygon points="0,62 892,8 892,300 0,300" fill="var(--navy)"/>
      <polygon points="0,60 892,6 892,14 0,68" fill="var(--white)"/>
      <polygon points="0,52 892,-2 892,7 0,61" fill="var(--gold-band)"/>
    </svg>

    <div class="portrait" role="img" aria-label="Portrait photo of Dan Marlowe"></div>

    <div class="contact">
      <p class="contact-name">Dan Marlowe</p>
      <p class="contact-role">Mediator</p>
      <p class="contact-detail contact-email">dmarlowe@harborline-adr.com</p>
      <p class="contact-detail">Phone: (555) 014-2290</p>
    </div>

    <div class="firm">
      <span class="firm-mark"></span>
      <span class="firm-name">Harborline Mediation</span>
    </div>
  </main>
</body>
</html>
```